bluecastle aquatics of northeast florida business card

I need a new attractive business card. I am planning on printing on very thick rounded corner stock and having painted edges. We are a swimming pool remodel, repair, and service company in north florida. Our current logo is red, white, and blue. It doesn't necessarily have to stay that way, I am open to other ideas. It will need to contain my name, work and cell numbers, email, website, and my contractor license number.

Target Market(s)

High end residential and commercial clients

Industry/Entity Type

Business

Contact Information for Business Card

Company name, employee name and title, work and cell phone numbers, email and website, and Contractor number.

our work scope should be on card somewhere: remodel ~ repair ~ service

logo or slight variation of logo also. (not necessarily set on keeping exact logo)

Colors

Designer to choose colors to be used in the design.

Requirements
Nice to have
• We deal with water so I think some sort of water element or just a color similar to pool water would be nice to integrate into design.

```html
<!DOCTYPE html>
<html lang="en">
<head>
<meta charset="utf-8">
<title>Bluecastle Aquatics – Business Card</title>
<link href="https://fonts.googleapis.com/css2?family=Open+Sans:ital,wght@0,400;0,600;0,700;1,400&display=swap" rel="stylesheet">
<style>
  :root {
    --backdrop: #262626;
    --card: #f6f9fd;
    --slate-light: #647ba1;
    --slate-dark: #34486a;
    --water-deep: #2d4568;
    --water-light: #9fb3cf;
    --name-blue: #4d6791;
    --text-grey: #555a61;
    --service-blue: #4f6a93;
  }
  * { margin: 0; padding: 0; box-sizing: border-box; }
  html, body { width: 1200px; height: 1000px; overflow: hidden; }
  body {
    background: var(--backdrop);
    font-family: "Open Sans", Arial, sans-serif;
    position: relative;
  }
  .card {
    position: absolute;
    top: 217px;
    width: 313px;
    height: 545px;
    background: var(--card);
    overflow: hidden;
    text-align: center;
  }
  .card--front { left: 237px; }
  .card--back { left: 636px; }
  .card__base { position: absolute; left: 0; bottom: 0; width: 313px; height: 545px; }

  .brand {
    position: absolute;
    left: 0; right: 0;
    color: var(--name-blue);
    font-size: 14px;
    font-weight: 600;
    letter-spacing: 1.5px;
    line-height: 19px;
    text-transform: uppercase;
  }
  .brand span { display: block; }

  .card--front .brand { top: 69px; }
  .person { position: absolute; top: 158px; left: 0; right: 0; }
  .person__name { font-size: 21px; font-weight: 700; color: var(--name-blue); letter-spacing: 0.3px; line-height: 28px; }
  .person__title { font-size: 20px; font-style: italic; color: var(--text-grey); line-height: 26px; }

  .contact { position: absolute; top: 239px; left: 0; right: 0; color: var(--text-grey); font-size: 17px; line-height: 26px; }
  .contact__phone { display: flex; justify-content: center; align-items: center; gap: 6px; }
  .contact__phone svg { width: 13px; height: 16px; fill: var(--name-blue); }
  .contact__web { margin-top: 17px; line-height: 22px; }

  .emblem { position: absolute; left: 87px; top: 63px; width: 138px; height: 138px; }
  .card--back .brand { top: 252px; }
  .licence { position: absolute; top: 303px; left: 0; right: 0; font-size: 14.5px; color: var(--text-grey); }
  .services { position: absolute; top: 332px; left: 0; right: 0; font-size: 15px; color: var(--service-blue); letter-spacing: 0.2px; }
  .services span { color: var(--text-grey); margin: 0 4px; }
</style>
</head>
<body>
  <svg width="0" height="0" style="position:absolute" aria-hidden="true">
    <defs>
      <linearGradient id="water" x1="0" y1="0" x2="1" y2="1">
        <stop offset="0" stop-color="#2d4568"/>
        <stop offset="0.5" stop-color="#9fb3cf"/>
        <stop offset="1" stop-color="#2d4568"/>
      </linearGradient>
    </defs>
  </svg>

  <section class="card card--front">
    <p class="brand"><span>Bluecastle Aquatics</span><span>of Northeast Florida</span></p>

    <div class="person">
      <p class="person__name">DANIEL WHITMORE</p>
      <p class="person__title">owner</p>
    </div>

    <div class="contact">
      <p class="contact__phone">
        <svg viewBox="0 0 13 16" aria-hidden="true"><path d="M2 1 L5 1 L6 5 L4 6.5 Q5.5 10 8 11.5 L9.5 10 L12.5 11.5 L12 15 Q5 15 1.5 8 Q0.5 4 2 1 Z"/></svg>
        012 345 6789
      </p>
      <p class="contact__phone">
        <svg viewBox="0 0 13 16" aria-hidden="true"><path d="M2.5 0 H10.5 Q12 0 12 1.5 V14.5 Q12 16 10.5 16 H2.5 Q1 16 1 14.5 V1.5 Q1 0 2.5 0 Z M3 2 V12.5 H10 V2 Z M6.5 13.3 a0.9 0.9 0 1 0 0.01 0 Z"/></svg>
        012 345 6789
      </p>
      <p class="contact__web">youremail@domain.com<br>www.yourwebsitename.com</p>
    </div>

    <svg class="card__base" viewBox="0 0 313 545">
      <polygon points="100,455 313,395 313,545 205,545" fill="url(#water)" role="img" aria-label="Rippling pool water photograph"/>
      <polygon points="0,377 100,455 0,485" fill="#647ba1"/>
      <polygon points="0,485 100,455 205,545 0,545" fill="#34486a"/>
    </svg>
  </section>

  <section class="card card--back">
    <svg class="emblem" viewBox="0 0 138 138">
      <circle cx="69" cy="69" r="69" fill="url(#water)" role="img" aria-label="Circle filled with rippling water texture"/>
    </svg>

    <p class="brand"><span>Bluecastle Aquatics</span><span>of Northeast Florida</span></p>

    <p class="licence">Licence 12345</p>
    <p class="services">REPAIR <span>|</span> REMODEL <span>|</span> SERVICE</p>

    <svg class="card__base" viewBox="0 0 313 545">
      <polygon points="0,395 220,452 110,545 0,545" fill="url(#water)" role="img" aria-label="Rippling pool water photograph"/>
      <polygon points="313,377 313,470 220,452" fill="#34486a"/>
      <polygon points="220,452 313,470 313,545 110,545" fill="#647ba1"/>
    </svg>
  </section>
</body>
</html>
```